Harbourline construction company Business card design

I need a business card design for my company. I have a logo but dont have business cards with our logo..

www.harbourlineconstructco.com.au

The logo is on the website

I need the same details as this design I have attached. we have changed the logo and colours. just like the website

Industry/Entity Type

Building

```html
<!DOCTYPE html>
<html lang="en">
<head>
<meta charset="utf-8">
<title>Harbourline construction company – Business card</title>
<link rel="stylesheet" href="https://fonts.googleapis.com/css2?family=Cinzel:wght@400;600&family=Oswald:wght@500&family=Open+Sans:wght@400&family=Tinos:wght@700&display=swap">
<style>
  :root {
    --page-bg: #ecebe8;
    --card-white: #ffffff;
    --panel-dark: #232323;
    --brand-blue: #3a8fd0;
    --text-grey: #9a9a9a;
    --rule-grey: #b5b5b5;
    --contact-light: #d6d6d6;
    --title-grey: #a8a8a8;
  }
  * { margin: 0; padding: 0; box-sizing: border-box; }
  html, body { width: 1200px; height: 1000px; overflow: hidden; }
  body {
    background: var(--page-bg);
    display: flex;
    align-items: center;
    justify-content: center;
  }
  .business-card {
    position: relative;
    width: 1000px;
    height: 610px;
    background: var(--card-white);
    border-radius: 56px;
    box-shadow: 0 10px 30px rgba(0,0,0,0.12);
    overflow: hidden;
  }
  .brand-side {
    position: absolute;
    left: 0; top: 0;
    width: 470px; height: 100%;
    display: flex;
    flex-direction: column;
    align-items: center;
    justify-content: center;
    padding-top: 20px;
  }
  .brand-mark {
    width: 64px; height: 64px;
    background: var(--brand-blue);
    margin-bottom: 26px;
  }
  .brand-name {
    font-family: "Cinzel", serif;
    font-weight: 600;
    font-size: 50px;
    letter-spacing: 1px;
    color: var(--brand-blue);
  }
  .brand-rule {
    width: 360px;
    height: 3px;
    background: var(--rule-grey);
    margin: 22px 0 12px;
  }
  .tagline {
    font-family: "Tinos", serif;
    font-weight: 700;
    font-size: 22px;
    line-height: 1.2;
    color: var(--text-grey);
    text-align: center;
  }
  .contact-panel {
    position: absolute;
    top: 26px; right: 26px; bottom: 26px;
    width: 470px;
    background: var(--panel-dark);
    padding: 40px 36px 0 40px;
  }
  .person-name {
    font-family: "Cinzel", serif;
    font-weight: 400;
    font-size: 38px;
    color: var(--brand-blue);
    letter-spacing: 1px;
  }
  .person-title {
    font-family: "Oswald", sans-serif;
    font-weight: 500;
    font-size: 22px;
    letter-spacing: 1px;
    color: var(--title-grey);
    margin-top: 2px;
  }
  .contact-list {
    list-style: none;
    margin-top: 64px;
  }
  .contact-item {
    display: flex;
    align-items: flex-start;
    gap: 18px;
    font-family: "Open Sans", sans-serif;
    font-size: 18px;
    color: var(--contact-light);
    margin-bottom: 16px;
    letter-spacing: 0.5px;
  }
  .contact-item.phone-numbers { letter-spacing: 4px; }
  .contact-icon { width: 30px; height: 30px; flex: none; }
  .address-lines { line-height: 1.5; }
</style>
</head>
<body>
  <div class="business-card">
    <section class="brand-side">
      <div class="brand-mark"></div>
      <div class="brand-name">Harbourline</div>
      <div class="brand-rule"></div>
      <p class="tagline">New Homes-Additions &amp; Renovations<br>Domestic &amp; Commercial Builders</p>
    </section>

    <section class="contact-panel">
      <h1 class="person-name">Marin Dovell</h1>
      <div class="person-title">Director</div>
      <ul class="contact-list">
        <li class="contact-item phone-numbers">
          <svg class="contact-icon" viewBox="0 0 30 30" aria-hidden="true"><rect x="4" y="6" width="22" height="20" rx="3" fill="#3a8fd0"/><rect x="8" y="2" width="14" height="6" rx="2" fill="#3a8fd0"/><g fill="#232323"><rect x="9" y="12" width="3" height="3"/><rect x="14" y="12" width="3" height="3"/><rect x="19" y="12" width="3" height="3"/><rect x="9" y="18" width="3" height="3"/><rect x="14" y="18" width="3" height="3"/><rect x="19" y="18" width="3" height="3"/></g></svg>
          <span>9410 2735<br>0412508634</span>
        </li>
        <li class="contact-item">
          <svg class="contact-icon" viewBox="0 0 30 30" aria-hidden="true"><rect x="8" y="1" width="14" height="28" rx="3" fill="#3a8fd0"/><rect x="10" y="5" width="10" height="18" fill="#232323"/><circle cx="15" cy="26" r="1.5" fill="#232323"/></svg>
          <span>info@harbourlineconstructco.com.au</span>
        </li>
        <li class="contact-item">
          <svg class="contact-icon" viewBox="0 0 30 30" aria-hidden="true"><rect x="1" y="6" width="28" height="18" fill="#3a8fd0"/><path d="M1 6 L15 17 L29 6" fill="none" stroke="#232323" stroke-width="2"/></svg>
          <span>www.harbourlineconstructco.com.au</span>
        </li>
        <li class="contact-item">
          <svg class="contact-icon" viewBox="0 0 30 30" aria-hidden="true"><circle cx="15" cy="15" r="13" fill="none" stroke="#3a8fd0" stroke-width="2.5"/><ellipse cx="15" cy="15" rx="6" ry="13" fill="none" stroke="#3a8fd0" stroke-width="2"/><line x1="2" y1="15" x2="28" y2="15" stroke="#3a8fd0" stroke-width="2"/><line x1="4" y1="9" x2="26" y2="9" stroke="#3a8fd0" stroke-width="1.5"/><line x1="4" y1="21" x2="26" y2="21" stroke="#3a8fd0" stroke-width="1.5"/></svg>
          <span class="address-lines">Unit 4 Level 2,18 Tallowood<br>Ave,Merriden,WA 6071</span>
        </li>
      </ul>
    </section>
  </div>
</body>
</html>
```